Book jacket for Drumlore

We need a book jacket design (hard cover front, back, spine, flaps; soft cover and eBook). for a social psychology book with the general cluelessness (being "out of it") of how people function both in their personal and social lives. This is the third book written by the author, a practicing psychiatrist, and the content centers on a single subject, people's lack of genuine emotional contact, their cluelessness with themselves and with current national and world events.

Target Market(s)

People who want to better understand the state the nation and world is in now, and what they can do about it.

Font styles to use
Serif
Sans Serif

Requirements
Must have
• Bold, eye-catching cover
Nice to have
• Like the idea of separating the title word (drum lore) to better emphasize the concept of lack of contact

```html
<!DOCTYPE html>
<html lang="en">
<head>
<meta charset="UTF-8">
<title>Drumlore — Book Jacket</title>
<link href="https://fonts.googleapis.com/css2?family=Bebas+Neue&display=swap" rel="stylesheet">
<style>
  :root {
    --stage: #262626;
    --sky-top: #1561b0;
    --sky-mid: #2a6fbe;
    --sky-bottom: #528cd4;
    --type-white: #ffffff;
    --feather-core: rgba(238, 244, 252, 0.85);
    --feather-edge: rgba(238, 244, 252, 0);
  }
  * { margin: 0; padding: 0; box-sizing: border-box; }
  html, body {
    width: 1200px;
    height: 1200px;
    overflow: hidden;
    background: var(--stage);
  }
  .canvas {
    position: relative;
    width: 1200px;
    height: 1200px;
    background: var(--stage);
  }
  .cover {
    position: absolute;
    left: 70px;
    top: 40px;
    width: 1060px;
    height: 1120px;
    background: linear-gradient(180deg, var(--sky-top) 0%, var(--sky-top) 38%, var(--sky-mid) 62%, var(--sky-bottom) 100%);
    overflow: hidden;
  }
  .cover-title {
    position: absolute;
    top: 118px;
    left: 0;
    width: 100%;
    text-align: center;
    font-family: "Bebas Neue", "Arial Narrow", sans-serif;
    font-size: 276px;
    line-height: 1;
    letter-spacing: 2px;
    color: var(--type-white);
  }
  .cover-feather {
    position: absolute;
    left: 218px;
    top: 612px;
    width: 618px;
    height: 340px;
    border-radius: 50% 60% 50% 40% / 40% 60% 50% 60%;
    background: radial-gradient(ellipse 55% 45% at 58% 50%, var(--feather-core) 0%, rgba(238,244,252,0.45) 55%, var(--feather-edge) 100%);
    transform: rotate(-14deg);
  }
  .cover-author {
    position: absolute;
    top: 938px;
    left: 0;
    width: 100%;
    text-align: center;
    font-family: "Bebas Neue", "Arial Narrow", sans-serif;
    font-size: 80px;
    line-height: 1;
    letter-spacing: 15px;
    padding-left: 15px;
    color: var(--type-white);
  }
</style>
</head>
<body>
  <main class="canvas">
    <section class="cover">
      <h1 class="cover-title">Drumlore</h1>
      <div class="cover-feather" role="img" aria-label="Photograph of a single white feather floating in a clear blue sky"></div>
      <p class="cover-author">Harold Vinter M.D.</p>
    </section>
  </main>
</body>
</html>
```